New stationery for photographic studio - logo already designed
Business cards, letterhead, comp slips, DVD face
New stationery for photographic studio - logo already designed -
Creative Brief
Use specific fonts
Handel Gothic
Simple
Dale Hoskins
Photographer
42 Pellow Lane Fareham Hampshire PO16 8RT
dalehoskins@tarnbrookstudios.co.uk
www.tarnbrookstudios.co.uk
My logo features the company name next to it in the .ai file. Ideally I would like the logo to just be presented on it's own with the company name mentioned elsewhere (Tarnbrook Studios). I also have a separate website for my commercial work www.tarnbrookcommercial.co.uk - which I will likely want to print additional business cards for to get some separation from the other side of the business (portraits) but with exactly the same look and feel just a text change.
Some of my cards will features images and so I need a single sided card design. However, some of them will also have a plain back and I was looking to have variant with just a logo on the back

```html
<!DOCTYPE html>
<html lang="en">
<head>
<meta charset="utf-8">
<title>Tarnbrook Studios – Stationery Set</title>
<link rel="stylesheet" href="https://fonts.googleapis.com/css2?family=Michroma&family=Roboto:wght@400;500&display=swap">
<style>
  :root{
    --backdrop:#c9c9c9;
    --paper:#ffffff;
    --charcoal:#3e3e41;
    --charcoal-soft:#525256;
    --steel-blue:#7f9cc6;
    --mist-blue:#e4ecf6;
    --mist-blue-2:#eef3f9;
    --brand-blue:#3f6ea8;
    --ink:#4a4a4a;
    --disc-grey:#dcdcdc;
  }
  *{box-sizing:border-box;margin:0;padding:0}
  html,body{width:1200px;height:562px;overflow:hidden;background:var(--backdrop)}
  .canvas{position:relative;width:1200px;height:562px;background:var(--backdrop);font-family:"Roboto",Arial,sans-serif;color:var(--ink)}
  .piece{position:absolute;background:var(--paper);overflow:hidden;box-shadow:0 1px 2px rgba(0,0,0,.15)}
  .piece svg.art{position:absolute;inset:0;width:100%;height:100%}
  .brand{position:absolute;display:flex;align-items:center;gap:5px;font-family:"Michroma",Arial,sans-serif;color:var(--brand-blue);letter-spacing:.04em;white-space:nowrap}
  .brand-square{display:inline-block;background:var(--steel-blue)}
  .brand.on-dark{color:var(--paper)}
  .small{position:absolute;font-size:5px;line-height:1.5;color:var(--ink);white-space:nowrap}

  .letterhead{left:19px;top:19px;width:370px;height:526px}
  .letterhead .brand{left:24px;top:34px;font-size:8px}
  .letterhead .brand-square{width:18px;height:18px}

  .comp-slip{left:420px;top:108px;width:389px;height:204px}
  .comp-slip .brand{left:14px;top:14px;font-size:7px}
  .comp-slip .brand-square{width:15px;height:15px}
  .comp-slip .small{left:14px;top:160px}

  .card{width:158px;height:84px}
  .card-front{left:835px;top:108px}
  .card-front .brand{left:8px;top:10px;font-size:5px}
  .card-front .brand-square{width:11px;height:11px}
  .card-front .person{position:absolute;right:8px;top:10px;text-align:right;font-family:"Michroma",Arial,sans-serif;font-size:5px;line-height:1.5;color:var(--brand-blue)}
  .card-back-plain{left:1010px;top:108px;background:var(--charcoal)}
  .card-dark{left:835px;top:211px;background:var(--charcoal)}
  .card-dark .brand{left:8px;top:10px;font-size:5px}
  .card-dark .brand-square{width:11px;height:11px}
  .card-dark .role{position:absolute;right:8px;top:11px;font-family:"Michroma",Arial,sans-serif;font-size:5px;color:var(--paper)}
  .card-dark .small{left:8px;top:56px;color:#e6e6e6;font-size:4px}
  .card-light{left:1010px;top:211px}

  .disc{position:absolute;top:343px;width:202px;height:202px}
  .disc-dark{left:432px}
  .disc-white{left:691px}
  .disc-grey{left:948px}
</style>
</head>
<body>
<main class="canvas">

  <!-- Letterhead -->
  <section class="piece letterhead" aria-label="Letterhead">
    <svg class="art" viewBox="0 0 370 526" preserveAspectRatio="none" aria-hidden="true">
      <path d="M0 0H370V88C300 58 200 24 0 12Z" fill="var(--charcoal)"/>
      <path d="M0 250C120 300 250 260 370 300V370C260 330 130 380 0 330Z" fill="var(--mist-blue-2)"/>
      <path d="M0 330C130 390 260 340 370 390V440C250 410 120 450 0 400Z" fill="var(--mist-blue)"/>
      <path d="M0 420C110 470 240 500 370 482V526H0Z" fill="var(--steel-blue)"/>
      <path d="M0 405C120 455 240 478 370 465V482C240 500 110 470 0 420Z" fill="var(--mist-blue)"/>
    </svg>
    <div class="brand"><span class="brand-square"></span>TARNBROOK STUDIOS</div>
  </section>

  <!-- Compliments slip -->
  <section class="piece comp-slip" aria-label="Compliments slip">
    <svg class="art" viewBox="0 0 389 204" preserveAspectRatio="none" aria-hidden="true">
      <path d="M0 0H389V68C300 42 180 18 0 6Z" fill="var(--charcoal)"/>
      <path d="M0 110C120 140 260 100 389 130V160C260 135 120 170 0 140Z" fill="var(--mist-blue-2)"/>
      <path d="M170 204C250 188 320 176 389 170V204Z" fill="var(--steel-blue)"/>
    </svg>
    <div class="brand"><span class="brand-square"></span>TARNBROOK STUDIOS</div>
    <p class="small">42 Pellow Lane Fareham Hampshire PO16 8RT<br>dalehoskins@tarnbrookstudios.co.uk<br>www.tarnbrookstudios.co.uk</p>
  </section>

  <!-- Business card front -->
  <section class="piece card card-front" aria-label="Business card front">
    <svg class="art" viewBox="0 0 158 84" preserveAspectRatio="none" aria-hidden="true">
      <path d="M0 58C50 70 110 52 158 64V84H0Z" fill="var(--mist-blue-2)"/>
    </svg>
    <div class="brand"><span class="brand-square"></span>TARNBROOK</div>
    <p class="person">Dale Hoskins<br>Photographer</p>
  </section>

  <!-- Business card plain back -->
  <section class="piece card card-back-plain" aria-label="Business card plain back">
    <svg class="art" viewBox="0 0 158 84" preserveAspectRatio="none" aria-hidden="true">
      <path d="M0 40C50 60 110 30 158 50V62C110 44 50 72 0 54Z" fill="var(--charcoal-soft)"/>
      <path d="M0 62C60 78 110 56 158 70V76C110 64 60 84 0 70Z" fill="var(--charcoal-soft)"/>
    </svg>
  </section>

  <!-- Business card dark variant -->
  <section class="piece card card-dark" aria-label="Business card dark variant">
    <svg class="art" viewBox="0 0 158 84" preserveAspectRatio="none" aria-hidden="true">
      <path d="M0 44C50 60 110 36 158 52V60C110 46 50 70 0 54Z" fill="var(--charcoal-soft)"/>
    </svg>
    <div class="brand on-dark"><span class="brand-square"></span>TARNBROOK</div>
    <p class="role">Photographer</p>
    <p class="small">Dale Hoskins<br>dalehoskins@tarnbrookstudios.co.uk<br>www.tarnbrookstudios.co.uk</p>
  </section>

  <!-- Business card light back -->
  <section class="piece card card-light" aria-label="Business card light back">
    <svg class="art" viewBox="0 0 158 84" preserveAspectRatio="none" aria-hidden="true">
      <path d="M60 84C100 70 130 50 158 44V84Z" fill="var(--mist-blue-2)"/>
    </svg>
  </section>

  <!-- DVD faces -->
  <svg class="disc disc-dark" viewBox="0 0 202 202" aria-label="DVD face, dark">
    <defs><clipPath id="disc-clip-a"><circle cx="101" cy="101" r="101"/></clipPath></defs>
    <circle cx="101" cy="101" r="101" fill="var(--charcoal)"/>
    <g clip-path="url(#disc-clip-a)">
      <path d="M0 80C60 110 140 60 202 100V120C140 84 60 130 0 100Z" fill="var(--charcoal-soft)"/>
      <path d="M0 130C70 160 140 120 202 150V162C140 136 70 174 0 144Z" fill="var(--charcoal-soft)"/>
    </g>
    <circle cx="101" cy="101" r="24" fill="var(--paper)"/>
  </svg>

  <svg class="disc disc-white" viewBox="0 0 202 202" aria-label="DVD face, white">
    <defs><clipPath id="disc-clip-b"><circle cx="101" cy="101" r="101"/></clipPath></defs>
    <circle cx="101" cy="101" r="101" fill="var(--paper)"/>
    <g clip-path="url(#disc-clip-b)">
      <path d="M0 120C70 150 140 110 202 140V160C140 130 70 170 0 140Z" fill="var(--mist-blue-2)"/>
    </g>
    <circle cx="101" cy="101" r="16" fill="none" stroke="#bfbfbf" stroke-width="1"/>
    <circle cx="101" cy="101" r="9" fill="var(--backdrop)"/>
  </svg>

  <svg class="disc disc-grey" viewBox="0 0 202 202" aria-label="DVD face, light grey">
    <defs><clipPath id="disc-clip-c"><circle cx="101" cy="101" r="101"/></clipPath></defs>
    <circle cx="101" cy="101" r="101" fill="var(--disc-grey)"/>
    <g clip-path="url(#disc-clip-c)">
      <path d="M0 110C70 140 140 100 202 130V150C140 120 70 160 0 130Z" fill="#e8e8e8"/>
    </g>
    <circle cx="101" cy="101" r="24" fill="var(--paper)"/>
  </svg>

</main>
</body>
</html>
```